Facebook Header Design Project.

I'm supplying white and colored logos. The Facebook page already exists. URL = https://www.pagebook.example/lumocrest.design The design should not be based on what's already there. Consider mobile implications of the design. This Design will form the designs of other social media headers. LumoCrest is a web design | digital marketing company.

Target Market(s)

People interested in web design | digital marketing services.

Industry/Entity Type

LumoCrest is a web design | digital marketing company. That should be clear in the design.

Colors
0054AA
0677BA
7BADD7
CADEEF
E8F1F8

Requirements
Must have
• Logo. Use Facebook header image dimension.
Nice to have
• Use a color scheme like the logo and feel free to add a color or two from the other side of the color whee.

```html
<!DOCTYPE html>
<html lang="en">
<head>
<meta charset="utf-8">
<title>LumoCrest — Cover Header</title>
<link rel="stylesheet" href="https://fonts.googleapis.com/css2?family=Montserrat:wght@600;700&display=swap">
<style>
  :root {
    --navy: #22479a;
    --brand: #0054aa;
    --mid: #0677ba;
    --sky: #7badd7;
    --pale: #cadeef;
    --mist: #e8f1f8;
    --paper: #f5f6f9;
    --band: #dfe3ef;
    --deep: #061a33;
    --glow: #1aa3d6;
  }
  html, body {
    margin: 0;
    padding: 0;
    overflow: hidden;
    background: #ffffff;
  }
  .cover {
    position: relative;
    width: 1200px;
    height: 457px;
    overflow: hidden;
    background: var(--paper);
    font-family: "Montserrat", Arial, sans-serif;
  }
  .cover__shapes {
    position: absolute;
    inset: 0;
  }
  .brand {
    position: absolute;
    left: 44px;
    top: 52px;
    display: flex;
    align-items: center;
    gap: 12px;
  }
  .brand__dot {
    width: 18px;
    height: 18px;
    border-radius: 50%;
    background: var(--brand);
  }
  .brand__name {
    font-size: 44px;
    font-weight: 700;
    color: var(--brand);
    letter-spacing: -0.5px;
    line-height: 1;
  }
  .services {
    position: absolute;
    left: 41px;
    top: 180px;
    margin: 0;
    font-size: 26px;
    font-weight: 700;
    line-height: 36.6px;
    color: var(--navy);
  }
  .services span { display: block; }
  .contact {
    position: absolute;
    left: 36px;
    top: 406px;
    display: flex;
    align-items: center;
    gap: 8px;
    font-size: 17.5px;
    font-weight: 600;
    color: var(--navy);
  }
  .contact__item {
    display: flex;
    align-items: center;
    gap: 7px;
  }
  .contact__icon {
    width: 22px;
    height: 22px;
    flex: none;
  }
</style>
</head>
<body>
<div class="cover">
  <svg class="cover__shapes" width="1200" height="457" viewBox="0 0 1200 457" aria-hidden="false">
    <defs>
      <linearGradient id="visualFill" x1="0" y1="0" x2="1" y2="1">
        <stop offset="0" stop-color="#0a2a4d"/>
        <stop offset="0.45" stop-color="#0d5f8e"/>
        <stop offset="0.75" stop-color="#0a3a63"/>
        <stop offset="1" stop-color="#061a33"/>
      </linearGradient>
      <linearGradient id="softBand" x1="0" y1="0" x2="1" y2="0">
        <stop offset="0" stop-color="#ffffff" stop-opacity="0"/>
        <stop offset="1" stop-color="#ffffff" stop-opacity="0.9"/>
      </linearGradient>
    </defs>

    <!-- soft background diagonals -->
    <polygon class="bg-band" points="520,0 700,0 560,457 380,457" fill="url(#softBand)" opacity="0.6"/>
    <polygon class="bg-band" points="600,0 660,0 520,457 460,457" fill="#ffffff" opacity="0.5"/>

    <!-- outer frame band around the visual -->
    <polygon class="visual-frame" points="752,0 1200,0 1200,457 740,457 640,235 650,215" fill="var(--band)"/>

    <!-- visual area -->
    <polygon class="visual" role="img" aria-label="Photo of a businessman tapping a tablet in front of a glowing digital city grid"
      points="778,0 1200,0 1200,457 762,457 664,236 672,218" fill="url(#visualFill)"/>

    <!-- service banner frame -->
    <polyline class="service-frame" points="88,153 653,153 498,349 0,349"
      fill="none" stroke="var(--navy)" stroke-width="4.5" stroke-linejoin="miter"/>
  </svg>

  <div class="brand">
    <div class="brand__dot"></div>
    <div class="brand__name">LumoCrest</div>
  </div>

  <h1 class="services">
    <span>Web Design &amp; Development,</span>
    <span>Search Engine Optimization,</span>
    <span>Graphic Design and</span>
    <span>Digital Marketing Services.</span>
  </h1>

  <div class="contact">
    <div class="contact__item">
      <svg class="contact__icon" viewBox="0 0 22 22" aria-hidden="true">
        <circle cx="11" cy="11" r="11" fill="var(--navy)"/>
        <path d="M7.2 5.6c.5-.4 1.1-.3 1.4.2l1.2 1.9c.3.5.2 1-.2 1.3l-.8.6c.6 1.5 1.7 2.7 3.2 3.4l.7-.8c.4-.4.9-.4 1.3-.1l1.9 1.3c.5.3.6 1 .2 1.4l-.8.9c-.6.6-1.5.8-2.3.5-3.2-1.2-5.6-3.7-6.7-6.9-.3-.8 0-1.7.6-2.3z" fill="#ffffff"/>
      </svg>
      <span>+1 555-018-0342</span>
    </div>
    <div class="contact__item">
      <svg class="contact__icon" viewBox="0 0 22 22" aria-hidden="true">
        <circle cx="11" cy="11" r="11" fill="var(--navy)"/>
        <rect x="5.5" y="6" width="11" height="7.5" rx="1" fill="none" stroke="#ffffff" stroke-width="1.6"/>
        <rect x="8.5" y="15" width="5" height="1.6" rx="0.5" fill="#ffffff"/>
      </svg>
      <span>www.lumocrest.example</span>
    </div>
  </div>
</div>
</body>
</html>
```